Reggie Vosburn - Free Personalised Health Consultation - "Every body walks its own path"

This flyer will be left on tables/seats at speaking events and seminars and used to attain leads.

Top half will have "SMS me for a FREE Personalised Health Consultation" and my picture (see www.reggievosburn.example and pick most engaging photo) and underneath my contact details. It must have lines with "Notes:" halfway down so people can take notes at the seminar and lines on the back with my contact details again and "Notes: with lines.

I am having a business card also being designed by Plotnest for same and would like the flyer and business card to carry a similar feel/look for consistency.

Below is the brief for the business card being designed:
Business Card for www.reggievosburn.example site. It is a trust site and I use it for 1:1 relatable connections. It is the one I use for building intimate 1:1 trust building and Exec Coaching Services and programs for high wealth individuals and corporates. I also have a commercial programmatic site of my personal health products and services and programs for main stream one to many. www.crossgenvitality.example that can also provoke thought for the www.reggievosburn.example business card. (mind you will get a separate business card for that site, but want to provide context). It has a logo which you may want to draw from in designing the reggievosburn business card which is personal and is about building my brand. There is also a reggievosburn personal KX page and reggievosburn business KX page. I am a Certified Talent Compass 4.1 Coach with Verrick and you can get a corporate brief of me on there to give you more context https://www.verricktalenthub.example/coach/en-us/directory?search=reggie

Target Market(s)

Exec, IT, Health conscious. Corporates wanting to run Health and Wellness programs. Those wanting to go from good to great. Millennials to Middleaged.

Industry/Entity Type

Health And Wellness

Font styles to use
Sans Serif
Other font styles liked:
• Arial and Calibri ok too

Colors

Designer to choose colors to be used in the design.

Requirements
Must have
• Picture of me - use best from www.reggievosburn.example or can send one you choose.
• Contact details like my buisness card being designed by you guys in separate project.
• Name: Reggie Vosburn
• email: reggie@reggievosburn.,example
• Phone: Australia +61 455 318 026 Singapore: +65 8342 1960
Nice to have
• Open to ideas

```html
<!DOCTYPE html>
<html lang="en">
<head>
<meta charset="utf-8">
<title>Reggie Vosburn – Health Consultation Notes Flyer</title>
<link rel="stylesheet" href="https://fonts.googleapis.com/css2?family=Archivo+Black&family=Arimo:wght@400;700&display=swap">
<style>
  :root {
    --backdrop: #000000;
    --paper: #ffffff;
    --brand-blue: #00b2e7;
    --ink: #000000;
    --soft-grey: #eeeeee;
    --faint-grey: #f1f1f1;
    --rule-grey: #c9c9c9;
    --photo-dark: #2a2a2a;
    --photo-mid: #8a8a8a;
    --accent-line: #5b4a9c;
  }
  html, body {
    margin: 0;
    padding: 0;
    width: 1200px;
    height: 835px;
    overflow: hidden;
    background: var(--backdrop);
  }
  .sheet {
    position: absolute;
    top: 77px;
    width: 483px;
    height: 682px;
    background: var(--paper);
    overflow: hidden;
  }
  .sheet--front { left: 88px; }
  .sheet--back { left: 629px; }
  .sheet svg { display: block; }
  .headline { font-family: "Archivo Black", "Arial Black", sans-serif; fill: var(--paper); }
  .headline .highlight { fill: var(--ink); }
  .name-mark { font-family: "Arimo", Arial, sans-serif; font-weight: 400; fill: var(--ink); }
  .name-mark--faint { fill: var(--faint-grey); }
  .web-link { font-family: "Arimo", Arial, sans-serif; font-weight: 700; fill: var(--brand-blue); }
  .contact-text { font-family: "Arimo", Arial, sans-serif; font-weight: 400; fill: var(--paper); }
  .note-rule { stroke: var(--rule-grey); stroke-width: 0.8; }
</style>
</head>
<body>

<section class="sheet sheet--front">
  <svg width="483" height="682" viewBox="0 0 483 682">
    <defs>
      <linearGradient id="portraitFade" x1="0" y1="0" x2="0" y2="1">
        <stop offset="0" stop-color="var(--photo-mid)"/>
        <stop offset="0.45" stop-color="var(--photo-dark)"/>
        <stop offset="0.8" stop-color="var(--photo-mid)"/>
        <stop offset="1" stop-color="#ffffff" stop-opacity="0"/>
      </linearGradient>
    </defs>

    <circle class="backdrop-circle" cx="95" cy="105" r="112" fill="var(--soft-grey)"/>
    <circle class="offer-circle" cx="311" cy="183" r="173" fill="var(--brand-blue)"/>

    <path role="img" aria-label="Portrait of Reggie Vosburn, smiling with arms crossed, in a black V-neck t-shirt"
          d="M0 150 L60 140 Q70 60 110 30 Q150 40 155 110 L165 170 Q225 190 260 270 L262 330 Q225 350 195 380 L185 430 L0 430 Z"
          fill="url(#portraitFade)"/>

    <circle class="name-circle" cx="245" cy="387" r="51" fill="var(--soft-grey)"/>

    <line x1="188" y1="81" x2="188" y2="271" stroke="var(--paper)" stroke-width="1"/>

    <text class="headline" x="200" y="111" font-size="40">SMS ME</text>
    <text class="headline" x="200" y="150" font-size="25">FOR A <tspan class="highlight">FREE</tspan></text>
    <text class="headline" x="200" y="190" font-size="25">PERSONALISED</text>
    <text class="headline" x="200" y="230" font-size="25">HEALTH</text>
    <text class="headline" x="200" y="270" font-size="25">CONSULTATION</text>

    <text class="name-mark" x="205" y="398" font-size="22" textLength="186" lengthAdjust="spacingAndGlyphs">Reggie Vosburn</text>
    <text class="web-link" x="431" y="419" font-size="8.5" text-anchor="end">WWW.REGGIEVOSBURN.EXAMPLE</text>

    <text class="name-mark name-mark--faint" x="12" y="645" font-size="54" textLength="450" lengthAdjust="spacingAndGlyphs">Reggie Vosburn</text>

    <g class="notes-lines">
      <line class="note-rule" x1="19" y1="475" x2="465" y2="475"/>
      <line class="note-rule" x1="19" y1="502" x2="465" y2="502"/>
      <line class="note-rule" x1="19" y1="529" x2="465" y2="529"/>
      <line class="note-rule" x1="19" y1="556" x2="465" y2="556"/>
      <line class="note-rule" x1="19" y1="583" x2="465" y2="583"/>
      <line class="note-rule" x1="19" y1="610" x2="465" y2="610"/>
      <line class="note-rule" x1="19" y1="637" x2="465" y2="637"/>
      <line class="note-rule" x1="19" y1="664" x2="465" y2="664"/>
    </g>
  </svg>
</section>

<section class="sheet sheet--back">
  <svg width="483" height="682" viewBox="0 0 483 682">
    <defs>
      <linearGradient id="portraitSmallFade" x1="0" y1="0" x2="0" y2="1">
        <stop offset="0" stop-color="#b5b5b5"/>
        <stop offset="0.6" stop-color="#6a6a6a"/>
        <stop offset="1" stop-color="#4a4a4a"/>
      </linearGradient>
    </defs>

    <g class="notes-lines">
      <line class="note-rule" x1="19" y1="32" x2="465" y2="32"/>
      <line class="note-rule" x1="19" y1="59" x2="465" y2="59"/>
      <line class="note-rule" x1="19" y1="86" x2="465" y2="86"/>
      <line class="note-rule" x1="19" y1="113" x2="465" y2="113"/>
      <line class="note-rule" x1="19" y1="140" x2="465" y2="140"/>
      <line class="note-rule" x1="19" y1="167" x2="465" y2="167"/>
      <line class="note-rule" x1="19" y1="194" x2="465" y2="194"/>
      <line class="note-rule" x1="19" y1="221" x2="465" y2="221"/>
      <line class="note-rule" x1="19" y1="248" x2="465" y2="248"/>
      <line class="note-rule" x1="19" y1="275" x2="465" y2="275"/>
      <line class="note-rule" x1="19" y1="302" x2="465" y2="302"/>
      <line class="note-rule" x1="19" y1="329" x2="465" y2="329"/>
      <line class="note-rule" x1="19" y1="356" x2="465" y2="356"/>
      <line class="note-rule" x1="19" y1="383" x2="465" y2="383"/>
      <line class="note-rule" x1="19" y1="410" x2="465" y2="410"/>
      <line class="note-rule" x1="19" y1="437" x2="465" y2="437"/>
      <line class="note-rule" x1="19" y1="464" x2="465" y2="464"/>
      <line class="note-rule" x1="83" y1="491" x2="465" y2="491"/>
      <line class="note-rule" x1="91" y1="518" x2="465" y2="518"/>
      <line class="note-rule" x1="111" y1="545" x2="465" y2="545"/>
      <line class="note-rule" x1="124" y1="572" x2="465" y2="572"/>
      <line class="note-rule" x1="134" y1="599" x2="465" y2="599"/>
    </g>

    <circle class="name-circle" cx="420" cy="653" r="77" fill="var(--soft-grey)"/>

    <path role="img" aria-label="Small portrait of Reggie Vosburn in a black t-shirt"
          d="M0 560 L20 548 Q25 480 52 470 Q80 478 80 535 L95 550 Q120 560 128 600 L128 620 L0 620 Z"
          fill="url(#portraitSmallFade)"/>

    <rect class="footer-blue" x="0" y="650" width="483" height="32" fill="var(--brand-blue)"/>
    <polygon class="footer-black" points="0,618 352,618 339,665 0,665" fill="var(--ink)"/>

    <g class="contact-block">
      <path d="M14 630 q1 -2 3 -1 l2 2 q1 1 0 2 l-1 1 q1 2 3 3 l1 -1 q1 -1 2 0 l2 2 q1 2 -1 3 q-4 1 -8 -3 q-4 -4 -3 -8 z" fill="var(--paper)"/>
      <text class="contact-text" x="29" y="636" font-size="8.5">AUSTRALIA:&#160; +61 455 318 026</text>
      <text class="contact-text" x="29" y="652" font-size="8.5">SINGAPORE: +65 8342 1960</text>

      <line x1="168" y1="625" x2="168" y2="657" stroke="var(--paper)" stroke-width="0.6"/>

      <rect x="177" y="630" width="8" height="6" fill="var(--paper)"/>
      <path d="M177 630 L181 633.5 L185 630" fill="none" stroke="var(--ink)" stroke-width="0.7"/>
      <text class="contact-text" x="190" y="636" font-size="8.5" textLength="142" lengthAdjust="spacingAndGlyphs">REGGIE@REGGIEVOSBURN.EXAMPLE</text>

      <circle cx="181" cy="648.5" r="4" fill="var(--paper)"/>
      <path d="M177 648.5 H185 M181 644.5 V652.5" stroke="var(--ink)" stroke-width="0.6"/>
      <text class="contact-text" x="190" y="652" font-size="8.5" textLength="134" lengthAdjust="spacingAndGlyphs">WWW.REGGIEVOSBURN.EXAMPLE</text>
    </g>

    <text class="name-mark" x="357" y="637" font-size="14" textLength="110" lengthAdjust="spacingAndGlyphs">Reggie Vosburn</text>
    <line x1="362" y1="648" x2="483" y2="648" stroke="var(--accent-line)" stroke-width="0.8"/>
  </svg>
</section>

</body>
</html>
```